Sprinkles & Tails 2nd Annual Fundraiser

I am a Realtor sponsoring the 2nd annual fundraiser on behalf of Allies of Harlow Vale Animal Haven. Like the flyer to be professional yet fun and inviting. Please see the attached file below. The 1st annual flyer was fun but not as professional, modern or inviting as I would have liked it to be.
Target Market(s)
Dog lovers in Ponte Vedra, Ponte Vedra Beach and Nocatee Florida
Logo Text
Needed
Font styles to use
Other font styles liked:
- Font that fits the style of the fundraiser
Colors
886aae
abd036
Requirements
Must have
- Please see the attached flyer and photos.
- This will be the 2nd Annual on Saturday, April 27, 2019 from 10AM - 1PM. Same location: Kendrick Realty, 418 Tillbrook Ave. Ponte Vedra FL 32075

```html
<!DOCTYPE html>
<html lang="en">
<head>
<meta charset="UTF-8">
<title>Sprinkles &amp; Tails – 2nd Annual Doggie Wash Extravaganza</title>
<link href="https://fonts.googleapis.com/css2?family=Jost:wght@400;500;600&family=Lato:wght@400;700&family=Playfair+Display:ital,wght@1,700&display=swap" rel="stylesheet">
<style>
  :root{
    --stage:#2a2623;
    --paper:#ffffff;
    --red:#d0202b;
    --charcoal:#2e2e30;
    --ink:#1b1b1b;
    --photo-warm:#8a7a68;
    --photo-cool:#6b7f86;
  }
  *{box-sizing:border-box;margin:0;padding:0}
  html,body{width:1200px;height:978px;overflow:hidden;background:var(--stage)}
  .stage{width:1200px;height:978px;display:flex;align-items:center;justify-content:center}
  .flyer{position:relative;width:700px;height:906px;background:var(--paper);overflow:hidden;font-family:"Lato",sans-serif;box-shadow:0 10px 30px rgba(0,0,0,.5)}

  .hero-photo{position:absolute;left:0;top:0;width:700px;height:372px;
    background:linear-gradient(160deg,#7d8a76 0%,#5d5a55 45%,#a79a88 100%)}
  .title-panel{position:absolute;right:0;top:88px;width:280px;height:284px;background:var(--red);
    color:#fff;text-align:center;padding:18px 22px 0;font-family:"Jost",sans-serif}
  .title-panel .edition{font-family:"Playfair Display",serif;font-style:italic;font-weight:700;font-size:19px;line-height:.95}
  .title-panel .rule{height:2px;background:#fff;margin:8px 0}
  .title-panel .name{font-weight:500;font-size:38px;line-height:1;letter-spacing:.5px;text-transform:uppercase}
  .title-panel .sub{font-weight:400;font-size:25px;line-height:1.05;text-transform:uppercase}
  .title-panel .tag{font-weight:400;font-size:21px;line-height:1.1;text-transform:uppercase;margin-top:6px}

  .photo-strip{position:absolute;left:0;top:376px;width:700px;height:126px;display:flex;gap:4px}
  .photo-strip .shot{flex:1}
  .shot.balloons{background:linear-gradient(135deg,#8aa070,#6d6a8e)}
  .shot.crowd{background:linear-gradient(135deg,#9aa3a6,#5f6a5f)}
  .shot.sign{background:linear-gradient(135deg,#2c2c34,#55525c)}
  .shot.companion{background:linear-gradient(135deg,#b88a5e,#d8d2c8)}

  .perks{position:absolute;left:0;top:502px;width:700px;height:92px;background:var(--red);color:#fff;
    font-family:"Jost",sans-serif;font-size:21px;text-align:center;padding-top:14px;line-height:1.45}

  .details{position:absolute;left:0;top:594px;width:410px;height:176px;padding:22px 26px;color:var(--red);
    font-family:"Lato",sans-serif;font-weight:700;font-size:15px;line-height:1.5}
  .details dl{display:grid;grid-template-columns:82px 1fr}
  .details .rain{margin-top:2px}

  .donate{position:absolute;right:0;top:594px;width:290px;height:176px;background:var(--charcoal);color:#fff;
    font-family:"Lato",sans-serif;font-size:12.5px;text-align:center;padding:26px 18px;line-height:1.45}
  .donate .url{margin-bottom:12px}

  .footer{position:absolute;left:0;top:770px;width:700px;height:136px;display:flex;align-items:center;padding:0 22px;gap:18px;color:var(--ink);font-size:12.5px;line-height:1.4}
  .footer .rule{position:absolute;left:22px;top:-2px;width:360px;height:2px;background:var(--ink)}
  .contact{flex:0 0 auto}
  .brand{display:flex;align-items:center;gap:6px;font-family:"Jost",sans-serif;font-weight:500;font-size:14px;color:var(--ink);line-height:1.15}
  .brand .dot{width:10px;height:10px;border-radius:50%;background:var(--red);flex:0 0 auto}
  .brand.haven{margin-left:auto;max-width:130px}
</style>
</head>
<body>
<div class="stage">
  <article class="flyer">
    <div class="hero-photo" role="img" aria-label="Photo of volunteers washing a shaggy dog on a driveway"></div>
    <header class="title-panel">
      <div class="edition">2nd<br>Annual</div>
      <div class="rule"></div>
      <h1 class="name">Sprinkles<br>&amp; Tails</h1>
      <div class="rule"></div>
      <p class="sub">Doggie Wash<br>Extravaganza</p>
      <div class="rule"></div>
      <p class="tag">A Family Fun Event<br>For All Ages</p>
    </header>

    <div class="photo-strip">
      <div class="shot balloons" role="img" aria-label="Photo of balloons and a free doggie wash sign"></div>
      <div class="shot crowd" role="img" aria-label="Photo of guests gathering with their dogs"></div>
      <div class="shot sign" role="img" aria-label="Photo of the event chalkboard sign"></div>
      <div class="shot companion" role="img" aria-label="Photo of a volunteer hugging a brown dog"></div>
    </div>

    <section class="perks">
      • FREE Doggie Wash • Raffle Drawings • Food &amp; Beverages<br>
      • Grand Prize • Vendors (FREE give-a-ways) • Donations Welcome
    </section>

    <section class="details">
      <dl>
        <dt>Date:</dt><dd>Saturday, April 27, 2019</dd>
        <dt>Time:</dt><dd>10AM - 1PM</dd>
        <dt>Location:</dt><dd>Kendrick Realty,</dd>
      </dl>
      <p>418 Tillbrook Ave. Ponte Vedra FL 32075</p>
      <p class="rain">(Rain date: Saturday, May 5th)</p>
    </section>

    <section class="donate">
      <p>To make a donation:</p>
      <p>https://www.pawsgiving.org/ahvah/</p>
      <p class="url">click: Donate</p>
      <p>All domestic breeds from puppies to seniors invited. Please be sure Furry Fido is tolerant of other dogs, crowds and bathing</p>
    </section>

    <footer class="footer">
      <div class="rule"></div>
      <div class="contact">
        Marissa Delano<br>Kendrick Realty Corp.<br>770.555.0182<br>marissadelano@kendrickrealtycorp.com
      </div>
      <div class="brand"><span class="dot"></span>Marissa Delano</div>
      <div class="contact">
        <strong>Janelle Ostrow</strong><br>AHVAH<br>904.555.0147<br>janelle-ostrow@mailbay.net
      </div>
      <div class="brand haven">Allies of Harlow Vale Animal Haven</div>
    </footer>
  </article>
</div>
</body>
</html>
```